Quenby Bespoke Furnishings logo and business card

Quenby is a female operated furniture design and reupholstery business. Working with luxury top end fabrics and furnishings for unique and stylish one off designs. Bringing loved pieces of furniture back to life by recovering on modern, trendy, stylish fabrics. Think Velvet chaise lounge or velour Chesterfield lounges, vibrant and unique colourful, individually designed statement pieces.
We would like a simple logo that can be used on socials and a business card that is simple yet striking . Possibly using a bronze or gold foil.
The business name is QUENBY BESPOKE FURNISHINGS
Can be just QUENBY
Logo will be used on socials and images of finished furniture.

Target Market(s)

high end luxury holiday houses. Artistic flair designer houses

Industry/Entity Type

Home Furniture

Contact Information for Business Card

Simple yet designer
Logo on the front and name details on the back

Font styles to use
Decorative

Requirements
Must have
• Finess
A feel of artistic design
Just a logo/business name on the front of the card
Should not have
• not a picture of furniture

```html
<!DOCTYPE html>
<html lang="en">
<head>
<meta charset="utf-8">
<title>Quenby Bespoke Furnishings – Business Card</title>
<link rel="stylesheet" href="https://fonts.googleapis.com/css2?family=Cinzel+Decorative:wght@700&family=Cinzel:wght@700&family=Cormorant+Garamond:wght@600&display=swap">
<style>
  :root {
    --stage: #2b2b2b;
    --bronze-top: #b98f66;
    --bronze-mid: #c0895a;
    --bronze-bottom: #c97f45;
    --ink: #2a1a10;
    --ivory: #fbf6ee;
  }
  * { box-sizing: border-box; margin: 0; padding: 0; }
  html, body { width: 1144px; height: 1200px; overflow: hidden; }
  body { background: var(--stage); position: relative; }

  .card {
    position: absolute;
    left: 178px;
    width: 714px;
    height: 415px;
    border-radius: 8px;
    overflow: hidden;
  }
  .card--back { top: 165px; }
  .card--front { top: 666px; }

  .card__surface {
    position: absolute; inset: 0;
    background: linear-gradient(180deg, var(--bronze-top) 0%, var(--bronze-mid) 55%, var(--bronze-bottom) 100%);
  }

  .card__frame { position: absolute; inset: 18px; }
  .card--back .card__frame { border: 6px solid var(--ink); }
  .card--back .card__frame::after {
    content: ""; position: absolute; inset: 4px;
    border: 1px solid var(--ink); opacity: .6;
  }
  .card--front .card__frame { inset: 15px; border: 6px solid var(--ivory); }

  .card__accent {
    position: absolute; width: 16px; height: 16px; border-radius: 50%;
    background: var(--ink);
  }
  .card--front .card__accent { background: var(--ivory); }
  .card__accent--tl { left: 84px; top: 36px; }
  .card__accent--br { right: 64px; bottom: 32px; }

  .card__details {
    position: absolute; left: 0; right: 0; top: 140px;
    text-align: center; color: var(--ink);
  }
  .brand-name {
    font-family: "Cinzel Decorative", "Cinzel", serif;
    font-weight: 700;
    letter-spacing: 2px;
    line-height: 1;
  }
  .card--back .brand-name { font-size: 44px; color: var(--ink); }
  .business-name {
    font-family: "Cinzel", serif; font-weight: 700;
    font-size: 24px; letter-spacing: .5px; margin-top: 10px;
  }
  .divider {
    width: 330px; height: 1px; background: var(--ink);
    margin: 8px auto 0; opacity: .8;
  }
  .phone {
    font-family: "Cormorant Garamond", serif; font-weight: 600;
    font-size: 22px; letter-spacing: 1.5px; margin-top: 8px;
  }

  .card__logo {
    position: absolute; left: 0; right: 0; top: 0; bottom: 0;
    display: flex; align-items: center; justify-content: center;
  }
  .card--front .brand-name { font-size: 100px; color: var(--ivory); letter-spacing: 4px; }
</style>
</head>
<body>
  <section class="card card--back" aria-label="Card back with contact details">
    <div class="card__surface" role="img" aria-label="Bronze foil background with fine scale pattern"></div>
    <div class="card__frame"></div>
    <span class="card__accent card__accent--tl" role="img" aria-label="Corner flourish"></span>
    <span class="card__accent card__accent--br" role="img" aria-label="Corner flourish"></span>
    <div class="card__details">
      <p class="brand-name">QUENBY</p>
      <p class="business-name">QUENBY BESPOKE FURNISHINGS</p>
      <div class="divider"></div>
      <p class="phone">TELL : 555-014-2290</p>
    </div>
  </section>

  <section class="card card--front" aria-label="Card front with logo">
    <div class="card__surface" role="img" aria-label="Bronze foil background with fine scale pattern"></div>
    <div class="card__frame"></div>
    <span class="card__accent card__accent--tl" role="img" aria-label="Corner flourish"></span>
    <span class="card__accent card__accent--br" role="img" aria-label="Corner flourish"></span>
    <div class="card__logo">
      <p class="brand-name">QUENBY</p>
    </div>
  </section>
</body>
</html>
```